Corroway Medical Imaging marketing poster

A poster to advertise our services. Something outstanding that catches the eye. Will be displayed at medical centres. Needs to advertise the following:
Opening hours - Mon-fri 8am-5:30pm Sat 8am-12:30
Services offered: Ultrasound, CT, Xray, Conebeam CT, Barium Studies, Injections and Biopsies, 3D/4D pregnancy scans.
We Bulk Bill concession card holders and under 18's
Locally owned and operated
www.corrowaymedicalimaging.example.au
include contact details also Tel: 96384027 Fax: 9638 4093

```html
<!DOCTYPE html>
<html lang="en">
<head>
<meta charset="utf-8">
<title>Corroway Medical Imaging – Services Poster</title>
<link rel="stylesheet" href="https://fonts.googleapis.com/css2?family=Questrial&family=Roboto+Condensed:wght@700&family=Arimo:wght@400&display=swap">
<style>
  :root {
    --blue: #3aa4dc;
    --green: #a2c83a;
    --ink: #1d1d1d;
    --paper: #ffffff;
    --panel: #f2f2f2;
    --footer: #232323;
    --stage: #e8e8e8;
    --photo-light: #f3ebe4;
    --photo-mid: #e2d6cc;
  }
  * { margin: 0; padding: 0; box-sizing: border-box; }
  html, body { width: 1113px; height: 1200px; overflow: hidden; background: var(--stage); }
  .poster {
    position: absolute; left: 153px; top: 20px;
    width: 859px; height: 1237px;
    transform: scale(0.938); transform-origin: 0 0;
    background: var(--paper); overflow: hidden;
    font-family: "Arimo", Arial, sans-serif; color: var(--ink);
  }
  .poster-shapes { position: absolute; inset: 0; }
  .brand {
    position: absolute; left: 92px; top: 382px; width: 270px; height: 270px;
    border-radius: 50%; background: var(--paper);
    display: flex; flex-direction: column; justify-content: center; align-items: center;
    font-family: "Questrial", sans-serif; color: var(--blue); text-align: center;
    line-height: 1.05;
  }
  .brand-name { font-size: 40px; letter-spacing: 1px; }
  .brand-sub { font-size: 22px; letter-spacing: 1px; }
  .hours-title {
    position: absolute; left: 35px; top: 690px;
    font-family: "Questrial", sans-serif; font-size: 44px;
  }
  .hours-line { position: absolute; left: 41px; top: 754px; font-size: 25px; }
  .hl { color: var(--blue); }
  .services-title {
    position: absolute; left: 185px; width: 488px; top: 858px;
    text-align: center; font-family: "Roboto Condensed", sans-serif;
    font-size: 34px; color: var(--blue); padding-bottom: 6px;
    border-bottom: 1px solid var(--blue);
  }
  .service {
    position: absolute; height: 54px; border-radius: 12px;
    display: flex; align-items: center; justify-content: center; text-align: center;
    font-family: "Roboto Condensed", sans-serif; font-size: 19px; line-height: 1.2;
    color: #fff; text-transform: uppercase;
  }
  .service.blue { background: var(--blue); }
  .service.green { background: var(--green); }
  .tagline {
    position: absolute; left: 0; width: 859px; top: 1150px;
    text-align: center; font-size: 18px;
  }
  .footer {
    position: absolute; left: 0; bottom: 0; width: 859px; height: 54px;
    background: var(--footer); color: #fff;
    display: flex; align-items: center; font-size: 17px; letter-spacing: 1px;
  }
  .contact { display: flex; align-items: center; gap: 18px; height: 100%; padding-left: 38px; }
  .contact + .contact { border-left: 2px solid #bbb; height: 38px; }
  .contact.tel { width: 218px; }
  .contact.fax { width: 217px; }
  .contact.web { letter-spacing: 0; font-size: 16px; }
  .icon { width: 30px; height: 30px; flex: none; }
</style>
</head>
<body>
<div class="poster">
  <svg class="poster-shapes" viewBox="0 0 859 1237" width="859" height="1237">
    <defs>
      <linearGradient id="photoTone" x1="0" y1="0" x2="1" y2="1">
        <stop offset="0" stop-color="var(--photo-light)"/>
        <stop offset="1" stop-color="var(--photo-mid)"/>
      </linearGradient>
    </defs>
    <path role="img" aria-label="Photo of a sonographer at an ultrasound machine with its monitor showing a scan"
          d="M0,0 H859 V612 C760,680 560,700 420,650 L100,440 C60,390 20,330 0,270 Z"
          fill="url(#photoTone)"/>
    <path d="M0,268 C25,330 60,390 100,440" stroke="var(--green)" stroke-width="4" fill="none"/>
    <path d="M320,640 C520,735 740,710 859,612 V672 C700,770 470,760 320,640 Z" fill="var(--green)"/>
    <path d="M0,800 C250,840 600,830 859,772 V1237 H0 Z" fill="var(--panel)"/>
  </svg>

  <div class="brand">
    <span class="brand-name">CORROWAY</span>
    <span class="brand-sub">MEDICAL IMAGING</span>
  </div>

  <h1 class="hours-title">Opening hours -</h1>
  <p class="hours-line">Mon-fri <span class="hl">8am-5:30pm</span> Sat <span class="hl">8am-12:30</span></p>

  <h2 class="services-title">OUR SERVICES OFFERED:</h2>
  <div class="service blue"  style="left:29px;  top:946px; width:182px;">Ultrasound</div>
  <div class="service green" style="left:235px; top:946px; width:182px;">Injections and<br>Biopsies</div>
  <div class="service blue"  style="left:441px; top:946px; width:182px;">Xray</div>
  <div class="service green" style="left:647px; top:946px; width:182px;">CT</div>
  <div class="service blue"  style="left:117px; top:1029px; width:196px;">Barium Studies</div>
  <div class="service green" style="left:335px; top:1029px; width:196px;">Conebeam CT,</div>
  <div class="service blue"  style="left:549px; top:1029px; width:206px;">3D/4D<br>Pregnancy Scans.</div>

  <p class="tagline">We Bulk Bill concession card holders and <span class="hl">under 18's</span>Locally owned and operated</p>

  <footer class="footer">
    <div class="contact tel">
      <svg class="icon" viewBox="0 0 30 30"><circle cx="15" cy="15" r="13" fill="none" stroke="#fff" stroke-width="2"/><path d="M10 8 l3 0 1 4 -2 1.5 c1 2.5 2.5 4 4.5 4.5 l1.5 -2 4 1 0 3 c-7 1 -13 -5 -12 -12z" fill="#fff"/></svg>
      <span>96384027</span>
    </div>
    <div class="contact fax">
      <svg class="icon" viewBox="0 0 30 30"><circle cx="15" cy="15" r="13" fill="none" stroke="#fff" stroke-width="2"/><rect x="10" y="7" width="10" height="5" fill="#fff"/><rect x="7" y="12" width="16" height="8" rx="1.5" fill="#fff"/><rect x="10" y="17" width="10" height="6" fill="#fff" stroke="var(--footer)" stroke-width="1"/></svg>
      <span>9638 4093</span>
    </div>
    <div class="contact web">
      <svg class="icon" viewBox="0 0 30 30" fill="none" stroke="#fff" stroke-width="1.5"><circle cx="15" cy="15" r="13" stroke-width="2"/><circle cx="15" cy="15" r="8"/><ellipse cx="15" cy="15" rx="3.5" ry="8"/><path d="M7 15 H23 M8.5 11 H21.5 M8.5 19 H21.5"/></svg>
      <span>www.corrowaymedicalimaging.example.au</span>
    </div>
  </footer>
</div>
</body>
</html>
```